New design for Vital Haven [Plonkit]

I manage a small web hosting company that I have been doing for many years, and I have quite a few clients that have been with me for a long time. A lot of them have extremely outdated websites such as the one this project is for " www.vitalhaven.com.au ". I am transferring all my clients over to Plonkit white-label. The website is very basic, it's only a small amount of links and a contact form.
I need a design that is up-to-date and attractive for today's standards, and of course plonkit compatible.
Thanks
Industry/Entity Type
It Company
Look and feel
Each slider illustrates characteristics of the customer's brand and the style your logo design should communicate.

```html
<!DOCTYPE html>
<html lang="en">
<head>
<meta charset="utf-8">
<title>Vital Haven</title>
<link rel="stylesheet" href="https://fonts.googleapis.com/css2?family=Questrial&family=Arimo:wght@400;700&display=swap">
<style>
:root{
  --ink:#1c1c1c;
  --body:#3a3a3a;
  --muted:#555;
  --brand-red:#d81414;
  --brand-navy:#1b2a6b;
  --pill-grey:#cfcfcf;
  --menu-bg:rgba(52,52,52,.9);
  --menu-text:#e6e6e6;
  --band:#ebebeb;
  --button:#2e2e2e;
  --rule:#c9c9c9;
  --field-border:#c8c8c8;
  --social:#2f6db5;
  --social-alt:#3aa4dc;
  --social-feed:#e98a1e;
}
*{box-sizing:border-box;margin:0;padding:0}
html,body{width:879px;height:1200px;overflow:hidden;background:#fff}
body{position:relative;font-family:Arimo,Arial,sans-serif;color:var(--body)}
.heading{font-family:Questrial,"Century Gothic",sans-serif;font-weight:400;color:var(--ink)}

.site-header{position:absolute;left:0;top:0;width:879px;height:97px;background:linear-gradient(#fff,#ececec);border-bottom:1px solid #d6d6d6}
.brand{position:absolute;left:12px;top:30px;display:flex;align-items:center;gap:8px;font-family:Questrial,sans-serif;font-size:27px;color:var(--brand-red)}
.brand-dot{width:12px;height:12px;border-radius:50%;background:var(--brand-navy)}

.main-nav{position:absolute;top:53px;left:0;width:879px;height:26px;font-family:Questrial,sans-serif;font-size:13px;color:var(--ink)}
.nav-item{position:absolute;top:0;height:26px;line-height:26px;display:flex;align-items:center;gap:6px}
.nav-item svg{width:10px;height:9px}
.nav-item.is-active{left:278px;width:103px;justify-content:center;border-radius:13px;background:linear-gradient(#ff3a3a,#c80b0b);color:#fff}
.nav-item.is-open{left:386px;width:148px;justify-content:center;border-radius:13px;background:var(--pill-grey)}
.dropdown{position:absolute;left:389px;top:84px;width:162px;height:178px;background:var(--menu-bg);border-radius:0 0 3px 3px;z-index:3;padding:12px 0 0 18px;list-style:none;font-family:Questrial,sans-serif;font-size:13px;color:var(--menu-text)}
.dropdown li{height:23px}

.hero{position:absolute;left:0;top:106px;width:879px;height:324px;background:radial-gradient(ellipse at 55% 55%,#d9a51f 0%,#a77613 40%,#4e3410 85%)}
.hero-arrow{position:absolute;top:256px;width:40px;height:40px;border-radius:50%;background:#1a1a1a;color:#fff;display:flex;align-items:center;justify-content:center;z-index:2}
.hero-arrow.prev{left:26px}.hero-arrow.next{left:813px}

.welcome{position:absolute;left:0;top:430px;width:879px;height:193px;background:var(--band)}
.welcome h1{position:absolute;left:34px;top:16px;font-size:26px}
.welcome p{position:absolute;left:34px;top:60px;width:822px;font-size:12.3px;line-height:19px;color:#2a2a2a}
.btn{position:absolute;height:26px;background:var(--button);color:#fff;font-size:12px;display:flex;align-items:center;justify-content:center}
.welcome .btn{left:771px;top:156px;width:81px}

.section-title{position:absolute;font-size:21px}
.lead{position:absolute;left:12px;top:680px;font-size:12.3px;color:#222}
.copy{position:absolute;left:12px;top:712px;width:520px;font-size:12.3px;line-height:17px;color:var(--muted)}
.advantage-photo{position:absolute;top:821px;width:225px;height:128px;background:linear-gradient(135deg,#d7b52a,#8a6a1c 60%,#3e3420)}
.advantage-text{position:absolute;top:962px;width:230px;font-size:11px;line-height:17px;color:var(--body)}
.divider{position:absolute;left:559px;top:650px;width:1px;height:403px;background:#d4d4d4}

.service{position:absolute;left:598px;width:250px}
.service h3{display:flex;align-items:center;gap:6px;font-size:11px;font-weight:700;color:#111}
.service p{margin:9px 0 0 4px;font-size:11px;line-height:17px;color:var(--body)}

.field{position:absolute;left:596px;width:253px;border:1px solid var(--field-border);background:#fff;font-size:11.5px;color:#888;padding:9px 12px}
.field.email{top:943px;height:30px;padding-top:8px}
.field.message{top:980px;height:82px}

.footer-rule{position:absolute;left:17px;top:1122px;width:845px;height:3px;background:var(--rule)}
.footer-links{position:absolute;left:0;width:879px;top:1140px;text-align:center;font-size:11.5px;color:#444;padding-right:0}
.footer-links span{position:relative;left:0}
.copyright{position:absolute;left:353px;top:1168px;font-size:11.5px;color:#444}
.connect{position:absolute;left:769px;top:1140px;font-size:11.5px;color:#333}
.social{position:absolute;top:1162px;width:21px;height:21px;border-radius:3px}
</style>
</head>
<body>

<header class="site-header">
  <div class="brand"><span class="brand-dot"></span>Vital Haven</div>
  <nav class="main-nav">
    <span class="nav-item is-active">About us</span>
    <span class="nav-item is-open">Products &amp; Services <svg viewBox="0 0 10 9"><path d="M1 1l4 3 4-3M1 5l4 3 4-3" fill="none" stroke="#333" stroke-width="1.5"/></svg></span>
    <span class="nav-item" style="left:550px">Projects &amp; Clients <svg viewBox="0 0 10 9"><path d="M1 1l4 3 4-3M1 5l4 3 4-3" fill="none" stroke="#333" stroke-width="1.5"/></svg></span>
    <span class="nav-item" style="left:687px">Whats new <svg viewBox="0 0 10 9"><path d="M1 1l4 3 4-3M1 5l4 3 4-3" fill="none" stroke="#333" stroke-width="1.5"/></svg></span>
    <span class="nav-item" style="left:792px">Contact Us <svg viewBox="0 0 10 9"><path d="M1 1l4 3 4-3M1 5l4 3 4-3" fill="none" stroke="#333" stroke-width="1.5"/></svg></span>
  </nav>
</header>

<ul class="dropdown">
  <li>Generator Sets</li>
  <li>Services &amp; Contracts</li>
  <li>Controls &amp; PLC’s</li>
  <li>Batteries &amp; Chaeges</li>
  <li>Upgrades</li>
  <li>Acoustic Enclosures</li>
  <li>Installation</li>
</ul>

<div class="hero" role="img" aria-label="Close-up photograph of a yellow industrial diesel generator engine"></div>
<span class="hero-arrow prev"><svg width="10" height="14" viewBox="0 0 10 14"><path d="M8 1L2 7l6 6" fill="none" stroke="#fff" stroke-width="2.5"/></svg></span>
<span class="hero-arrow next"><svg width="10" height="14" viewBox="0 0 10 14"><path d="M2 1l6 6-6 6" fill="none" stroke="#fff" stroke-width="2.5"/></svg></span>

<section class="welcome">
  <h1 class="heading">Welcome to Vital Haven</h1>
  <p>There are many variations of passages of Lorem Ipsum available, but the majority have suffered alteration in some form, by injected humour, or ran-domised words which don't look even slightly believable. If you are going to use a passage of Lorem Ipsum, you need to be sure there isn't anything embarrassing hidden in the middle of text. All the Lorem Ipsum generators on the Internet tend to repeat predefined chunks as necessary, making this the first true generator on the Internet. It uses a dictionary of over 200 Latin words, combined with a handful of model sentence structures, to generate Lorem Ipsum which looks reasonable</p>
  <span class="btn">Read more</span>
</section>

<h2 class="heading section-title" style="left:12px;top:643px">Industry Guid</h2>
<p class="lead">There are many variations of passages of Lorem Ipsum available, but the majority.</p>
<p class="copy">All the Lorem Ipsum generators on the Internet tend to repeat predefined chunks as necessary, making this the first true generator on the Internet. It uses a dictionary of over 200 Latin words, combined with a handful of model sentence structures.</p>

<h2 class="heading section-title" style="left:12px;top:780px">Our Advantages</h2>
<div class="advantage-photo" style="left:22px;background:linear-gradient(90deg,#9a9a9a 0%,#b0aca0 40%,#e3c21f 75%,#c9a614)" role="img" aria-label="Photograph of a grey and yellow portable generator set"></div>
<div class="advantage-photo" style="left:298px" role="img" aria-label="Photograph of a yellow diesel generator in a workshop"></div>
<p class="advantage-text" style="left:23px">Lalesua kertase mertyuade ioner grda anasera lorem suaskase agned laorem leot tellus dolobus eget kelementum vel, cursusle-ifend elitenean auctor wisi et umaliquam erat volutpat.</p>
<p class="advantage-text" style="left:298px">Lalesua kertase mertyuade ioner grda anasera lorem suaskase agned laorem leot tellus dolobus eget kelementum vel, cursusle-ifend elitenean auctor wisi et umaliquam erat volutpat.</p>
<span class="btn" style="left:159px;top:1062px;width:82px">Read more</span>
<span class="btn" style="left:435px;top:1062px;width:82px">Read more</span>

<div class="divider"></div>

<h2 class="heading section-title" style="left:600px;top:643px">Popular Service</h2>
<div class="service" style="top:681px">
  <h3><svg width="16" height="10" viewBox="0 0 16 10"><circle cx="2" cy="5" r="1.6" fill="#777"/><path d="M5 5h7" stroke="#777" stroke-width="2.5"/><path d="M10 1l5 4-5 4z" fill="#777"/></svg>New Technologies</h3>
  <p>Lorem Ipsum is simply dummy text of the printing and typesetting industry.</p>
</div>
<div class="service" style="top:754px">
  <h3><svg width="16" height="10" viewBox="0 0 16 10"><circle cx="2" cy="5" r="1.6" fill="#777"/><path d="M5 5h7" stroke="#777" stroke-width="2.5"/><path d="M10 1l5 4-5 4z" fill="#777"/></svg>Resources</h3>
  <p>Lorem Ipsum is simply dummy text of the printing and typesetting industry.</p>
</div>
<div class="service" style="top:827px">
  <h3><svg width="16" height="10" viewBox="0 0 16 10"><circle cx="2" cy="5" r="1.6" fill="#777"/><path d="M5 5h7" stroke="#777" stroke-width="2.5"/><path d="M10 1l5 4-5 4z" fill="#777"/></svg>Leadership</h3>
  <p>Lorem Ipsum is simply dummy text of the printing and typesetting industry.</p>
</div>

<h2 class="heading section-title" style="left:600px;top:909px">Quick Message</h2>
<div class="field email">Your E-mail</div>
<div class="field message">Message</div>
<span class="btn" style="left:767px;top:1071px;width:82px">Send</span>

<div class="footer-rule"></div>
<p class="footer-links">About us | Products &amp; Services | Projects &amp; Clients | Whats new | Contact Us</p>
<p class="copyright">All © Copyrights.VitalHaven.Resreved</p>
<p class="connect">Connect with us:</p>
<span class="social" style="left:780px;background:var(--social)"></span>
<span class="social" style="left:805px;background:var(--social-alt)"></span>
<span class="social" style="left:830px;background:var(--social-feed)"></span>

</body>
</html>
```